Glofarvik - Start-up company selling electricity

Hello let me tell you about Glofarvik.

Glofarvik is start-up company selling electricity in Iceland. The operations of the company consist of making power usage forecasts for our customers, purchasing the electricity wholesale from the energy producers, and selling the electricity to the consumer. We are focused on tech by using optimization and machine learning to minimize electricity prices to our customers. Our marketing strategy is to portray a tech company mindset and to show dedication to driving down the electricity price on the market.

We need your help to make our website pop. Possible concepts to work with are as follows:

- Iceland the land of ice and fire
- Green energy
- Innovation
- Tech and data science

Link to our website: https://prufa.glofarvik-example.is/
We are open to ideas.
Thank you!

Target Market(s)

Electricity consumers both homes and companies.

Number of Pages Required

1 page

Font styles to use
Serif
Sans Serif

```html
<!DOCTYPE html>
<html lang="is">
<head>
<meta charset="utf-8">
<title>Glofarvik – Sama rafmagn, bara ódýrara</title>
<link href="https://fonts.googleapis.com/css2?family=Poppins:wght@300;400&family=Tinos:wght@700&display=swap" rel="stylesheet">
<style>
:root{
  --navy:#142f59;
  --navy-deep:#132f58;
  --red:#a02a22;
  --grey:#6d6d6d;
  --ink:#333;
  --text:#555;
  --bg:#fafafa;
  --white:#fff;
}
*{margin:0;padding:0;box-sizing:border-box}
html,body{width:1200px;height:1112px;overflow:hidden;background:var(--bg)}
body{position:relative;font-family:'Poppins',sans-serif;color:var(--text)}
.abs{position:absolute}
.serif{font-family:'Tinos',serif;font-weight:700}
a{text-decoration:none}

.brand{left:161px;top:24px;display:flex;align-items:center;gap:10px}
.brand-dot{width:34px;height:34px;border-radius:50%;background:var(--navy)}
.brand-name{font-size:29px;color:var(--red);letter-spacing:.5px}
.nav{top:32px;font-size:13.5px;color:#111}

.hero-title{left:0;width:1200px;top:110px;text-align:center;font-size:37px;color:var(--ink);letter-spacing:.3px}

.badge{width:90px;height:90px;border-radius:50%;border:1.5px solid;background:var(--bg);
  box-shadow:5px 6px 7px rgba(0,0,0,.18);display:flex;align-items:center;justify-content:center}
.badge svg{width:50px;height:50px;fill:none;stroke:currentColor;stroke-width:1.8;stroke-linecap:round;stroke-linejoin:round}
.badge--navy{color:var(--navy);border-color:var(--navy)}
.badge--red{color:var(--red);border-color:var(--red)}
.badge--grey{color:var(--grey);border-color:var(--grey)}

.heading{font-size:20px;letter-spacing:.4px}
.copy{font-size:12px;line-height:20px;font-weight:300;color:#444;width:325px}
.btn{height:34px;display:flex;align-items:center;justify-content:center;font-size:15px;border-radius:3px}
.btn--navy{background:var(--navy);color:var(--white)}
.btn--outline{border:1px solid var(--navy);color:var(--navy)}
.btn--red{background:var(--red);color:var(--white)}
.btn--grey{background:var(--grey);color:var(--white)}

.price{font-size:25px;color:#333;font-weight:300}
.unit{font-size:12px;color:#555;font-weight:300}
.divider{left:396px;top:424px;width:1px;height:48px;background:#aaa}
.note{font-size:12px;color:#555;font-weight:300}

.visual{left:680px;top:208px;width:340px;height:512px;border-radius:10px;
  background:linear-gradient(180deg,#c6553a 0%,#a8412d 30%,#1c3a6a 55%,#0c1f44 100%)}

.footer{left:0;top:802px;width:1200px;height:272px;background:var(--navy-deep)}
.contact{width:280px;text-align:center;color:var(--white)}
.contact-icon{display:block;width:48px;height:75px;margin:0 auto}
.contact-title{margin-top:18px;font-size:18px;letter-spacing:.4px;line-height:24px}
.contact-text{margin-top:4px;font-size:12.5px;font-weight:300;line-height:20px}
.legal{left:0;top:1074px;width:1200px;height:38px;background:var(--red);color:var(--white);font-size:12.5px;font-weight:300}
.legal span{position:absolute;top:11px}
</style>
</head>
<body>

<header>
  <div class="abs brand"><span class="brand-dot"></span><span class="brand-name serif">GLOFARVIK</span></div>
  <nav>
    <span class="abs nav" style="left:617px">Viðskiptaskilmálar</span>
    <span class="abs nav" style="left:788px">Spurt &amp; Svarað</span>
    <span class="abs nav" style="left:936px">Um Glofarvik</span>
  </nav>
</header>

<h1 class="abs hero-title serif">SAMA RAFMAGN ~ BARA ÓDÝRARA!</h1>

<section>
  <div class="abs badge badge--navy" style="left:161px;top:208px">
    <svg viewBox="0 0 48 48"><path d="M4 22l8-8 6 2"/><path d="M44 22l-8-8-8 3-8 6c-2 2 0 5 3 3l5-3 9 9"/><path d="M12 14l-2 12 10 10c2 2 5-1 3-3M16 30l7 7c2 2 5-1 3-3M20 27l8 8c2 2 5-1 3-3l-4-4"/><path d="M24 6v5M17 8l2 4M31 8l-2 4"/></svg>
  </div>
  <h2 class="abs heading serif" style="left:285px;top:208px;color:var(--navy)">Velkomin Í Viðskipti</h2>
  <p class="abs copy" style="left:282px;top:240px">Lorem ipsum dolor sit amet, consectetuer adipiscing elit, sed diam nonummy nibh euismod</p>
  <a class="abs btn btn--navy" style="left:282px;top:294px;width:105px">Fyrirtæki</a>
  <a class="abs btn btn--outline" style="left:399px;top:294px;width:108px">Heimili</a>
</section>

<section>
  <div class="abs badge badge--red" style="left:161px;top:390px">
    <svg viewBox="0 0 48 48"><path d="M28 38H12V8h14l6 6v8"/><path d="M26 8v6h6M16 20h10M16 25h8M16 30h6"/><circle cx="33" cy="33" r="8"/><path d="M35 30h-3a1.5 1.5 0 000 3h2a1.5 1.5 0 010 3h-3M33 28v2M33 36v2"/></svg>
  </div>
  <h2 class="abs heading serif" style="left:282px;top:384px;color:var(--red)">Verðskrá</h2>
  <span class="abs price" style="left:300px;top:418px">6.95</span>
  <span class="abs unit" style="left:286px;top:454px">krónur / kWst</span>
  <span class="abs divider"></span>
  <span class="abs price" style="left:439px;top:418px">6.22</span>
  <span class="abs unit" style="left:424px;top:454px">krónur / kWst</span>
  <span class="abs note" style="left:286px;top:486px">Rafmagnskynding</span>
  <span class="abs note" style="left:287px;top:509px">Gerðu verðsamanburð</span>
  <a class="abs btn btn--red" style="left:449px;top:489px;width:105px">Verðvaki</a>
</section>

<section>
  <div class="abs badge badge--grey" style="left:161px;top:583px">
    <svg viewBox="0 0 48 48"><path d="M18 10a16 16 0 000 28M30 10a16 16 0 010 28"/><path d="M27 6l-9 20h8l-5 16 11-22h-8z"/></svg>
  </div>
  <h2 class="abs heading serif" style="left:283px;top:580px;color:#444">Framtíðin Er Spennandi</h2>
  <p class="abs copy" style="left:282px;top:612px">Gerum raforkukerfið snallara saman. Glofarvik notar gervigreind, gagnavísindi og sjálfvirkni til að lágmarka kostnað og stuðla að okrujöfnuði</p>
  <a class="abs btn btn--grey" style="left:282px;top:686px;width:105px">Vita Meira</a>
</section>

<div class="abs visual" role="img" aria-label="Photo collage of a glowing sunset over glacier ice above a night-blue globe with network lines"></div>

<footer class="abs footer">
  <div class="abs contact" style="left:194px;top:60px">
    <svg class="contact-icon" viewBox="0 0 48 75"><path d="M24 0C18 14 0 34 0 51a24 24 0 0048 0C48 34 30 14 24 0z" fill="#a02a22"/><path transform="translate(14 42) scale(.85)" fill="#fff" d="M6.6 10.8a15 15 0 006.6 6.6l2.2-2.2a1 1 0 011-.25 11.4 11.4 0 003.6.57 1 1 0 011 1V20a1 1 0 01-1 1A17 17 0 013 4a1 1 0 011-1h3.5a1 1 0 011 1c0 1.25.2 2.45.57 3.57a1 1 0 01-.25 1z"/></svg>
    <div class="contact-title serif">Kalla</div>
    <div class="contact-text">400-1234</div>
  </div>
  <div class="abs contact" style="left:459px;top:60px">
    <svg class="contact-icon" viewBox="0 0 48 75"><path d="M24 0C18 14 0 34 0 51a24 24 0 0048 0C48 34 30 14 24 0z" fill="#a02a22"/><path transform="translate(14 40) scale(.85)" fill="#fff" d="M12 2a7 7 0 00-7 7c0 5 7 13 7 13s7-8 7-13a7 7 0 00-7-7zm0 9.5A2.5 2.5 0 1112 6.5a2.5 2.5 0 010 5z"/></svg>
    <div class="contact-title serif">Heimilisfang</div>
    <div class="contact-text">Lindargata 42 170 Norðurnesi</div>
  </div>
  <div class="abs contact" style="left:720px;top:60px">
    <svg class="contact-icon" viewBox="0 0 48 75"><path d="M24 0C18 14 0 34 0 51a24 24 0 0048 0C48 34 30 14 24 0z" fill="#a02a22"/><path transform="translate(14 41) scale(.85)" fill="#fff" d="M3 6h18v1.5l-9 5.5-9-5.5zM3 9.5l9 5.5 9-5.5V18H3z"/></svg>
    <div class="contact-title serif">Póstur</div>
    <div class="contact-text">samband@glofarvik-example.is</div>
  </div>
</footer>

<div class="abs legal">
  <span style="left:163px">Höfundarréttur © Glofarvik 2021. Öll Réttindi Áskilin</span>
  <span style="right:163px">Copyright © Glofarvik 2021. Allur Réttur Askilin</span>
</div>

</body>
</html>
```